Black Car Limousine transportation business in Naples Florida

Brightway stand for my reliability and DPR stands for Devotion, P and R are the first initials of my children's names. It should show professionalism and a dedication to customer service. We keep our clients identities private. Show our professionalism. We are Black car Black tie company. We service transportation on a reserve basis to and from residents, airports, casinos, hotels,

Target Market(s)

It is a Private car service. High end clients. Businesses, Celebrity and athletes. Service to airports, hotels, special events.

Industry/Entity Type

Business

Contact Information for Business Card

A pearl metallic or Luster card. Standard business card size. Would like the name, Company email, show we take credit cards and phone number. Currently I don't have a website but will like to add later.

Logo Text

BRIGHTWAY DPR TRANSPORTATION

Font styles to use
Serif

Colors
eaeaea
000000

Requirements
Must have
• Must have Company email, show we take credit cards and phone number. Currently I don't have a website but will like to add later.
Nice to have
• Would like to stay with a black and white theme. Open to some color trim.
Should not have
• Open to suggestions

```html
<!DOCTYPE html>
<html lang="en">
<head>
<meta charset="utf-8">
<title>Brightway DPR Transportation – Business Card</title>
<link rel="stylesheet" href="https://fonts.googleapis.com/css2?family=Open+Sans:wght@400;600&display=swap">
<style>
  :root {
    --ink: #0b0b0b;
    --pearl: #eaeaea;
    --paper: #ffffff;
    --muted: #a4a4a4;
    --stage: #d9d6d1;
  }
  * { margin: 0; padding: 0; box-sizing: border-box; }
  html, body {
    width: 1200px;
    height: 1020px;
    overflow: hidden;
    background: var(--stage);
    font-family: "Open Sans", sans-serif;
  }
  .canvas {
    position: relative;
    width: 1200px;
    height: 1020px;
  }
  .card {
    position: absolute;
    left: 180px;
    width: 840px;
    height: 480px;
    overflow: hidden;
    box-shadow: 0 10px 28px rgba(0,0,0,.28);
  }
  .card--back { top: 20px; background: linear-gradient(135deg, #1b1b1b, var(--ink) 60%); }
  .card--front { top: 520px; background: linear-gradient(160deg, var(--paper) 55%, var(--pearl)); }

  /* Wordmark: one colour, one weight */
  .wordmark {
    position: absolute;
    font-weight: 400;
    line-height: 1;
    text-align: right;
    white-space: nowrap;
  }
  .wordmark span { display: block; }
  .wordmark__lead { font-size: 28px; }
  .wordmark__initials { font-size: 92px; letter-spacing: -2px; margin-top: -4px; }
  .wordmark__trade { font-size: 24px; letter-spacing: 10px; margin-top: 6px; margin-right: -10px; }

  .card--back .wordmark { color: var(--pearl); left: 50%; top: 50%; transform: translate(-50%, -50%); }
  .card--front .wordmark { color: var(--ink); right: 48px; bottom: 46px; }

  .holder {
    position: absolute;
    left: 46px;
    top: 40px;
    padding-left: 18px;
    border-left: 6px solid var(--ink);
  }
  .holder__name { font-size: 30px; font-weight: 400; color: #333; line-height: 1.05; }
  .holder__title { font-size: 17px; color: var(--muted); }

  .contacts {
    position: absolute;
    left: 46px;
    bottom: 46px;
    list-style: none;
    color: var(--ink);
    font-size: 19px;
  }
  .contacts li { display: flex; align-items: center; gap: 14px; margin-top: 12px; }
  .contacts svg { width: 24px; height: 20px; fill: var(--ink); flex: none; }
</style>
</head>
<body>
<main class="canvas">

  <section class="card card--back" aria-label="Card back">
    <div class="wordmark">
      <span class="wordmark__lead">Brightway</span>
      <span class="wordmark__initials">DPR</span>
      <span class="wordmark__trade">TRANSPORTATION</span>
    </div>
  </section>

  <section class="card card--front" aria-label="Card front">
    <div class="holder">
      <p class="holder__name">Your Name</p>
      <p class="holder__title">Job Title</p>
    </div>

    <ul class="contacts">
      <li>
        <svg viewBox="0 0 24 20" aria-hidden="true">
          <path d="M2 6c0-2 4-4 10-4s10 2 10 4v2h-5V6.5C15.5 6 8.5 6 7 6.5V8H2z"/>
          <path d="M5 9h14l2 9H3zM12 11a3 3 0 1 0 0 6 3 3 0 1 0 0-6z"/>
        </svg>
        <span>000 000 0000</span>
      </li>
      <li>
        <svg viewBox="0 0 24 20" aria-hidden="true">
          <path d="M1 3h22v1.5L12 11 1 4.5zM1 6.5l11 6.5 11-6.5V17H1z"/>
        </svg>
        <span>youremail@brightwaydpr.com</span>
      </li>
      <li>
        <svg viewBox="0 0 24 20" aria-hidden="true">
          <path d="M1 3h22v4H1zM1 9h22v8H1zM3 12v2h6v-2z" fill-rule="evenodd"/>
        </svg>
        <span>Major credit cards accepted</span>
      </li>
    </ul>

    <div class="wordmark">
      <span class="wordmark__lead">Brightway</span>
      <span class="wordmark__initials">DPR</span>
      <span class="wordmark__trade">TRANSPORTATION</span>
    </div>
  </section>

</main>
</body>
</html>
```